New Outdoor Fitness Flyer Project

Hi, we need a flyer design in A5 side (one sided preferably) for a new company based in Singapore called "Tide Motion". We are an outdoor based fitness company who offer personal training for 1 on 1 clients, kickboxing, HIIT (high intensity interval training), group classes out door based training. Catering for all fitness levels & age groups. Please view our website www.tidemotion-sg.example for more details.

As we are new to the industry, we need the flyer as our major advertising for now so the needs to pop and catch peoples attention.

Our logos are uploaded for usage for design of flyer.

Target Market(s)

We would love to target anyone with any fitness level.

Industry/Entity Type

Advertising

Requirements
Must have
• -types of trainings we offer (such as 1 on 1 Personal Training, Buddy Training, Kick boxing & Outdoor Group classes)

-we cater to all fitness level and age group.

-Anytime, Anywhere, At Your Own Convenience.

-Tagline (please choose one which is more suitable for the design): "Archive Faster Weight Loss & Muscle Gain", "Better Lifestyle Starts With Healthy Workout" or "Be Fit.Be Strong."

-our contact details:
M: 8164-5290
E: daniel@tidemotion-sg.example
W: www.tidemotion-sg.example

-call us now for a free trial! terms & conditions apply
Nice to have
• Please include pictures not given on our website as we would like to have something different.

```html
<!DOCTYPE html>
<html lang="en">
<head>
<meta charset="utf-8">
<title>Tide Motion – Outdoor Fitness Flyer</title>
<link rel="stylesheet" href="https://fonts.googleapis.com/css2?family=Arimo:ital,wght@0,400;0,700;1,700&family=EB+Garamond:ital@1&family=Merriweather:wght@700&family=Parisienne&family=Playball&display=swap">
<style>
  :root {
    --magenta: #d8137f;
    --purple: #6a2d91;
    --purple-deep: #4a1d6a;
    --frame: #a46be6;
    --ink: #1c1c1c;
    --tan: #c29362;
    --brown: #8a5a2c;
    --white: #ffffff;
  }
  * { margin: 0; padding: 0; box-sizing: border-box; }
  html, body { width: 846px; height: 1200px; overflow: hidden; background: var(--white); }
  .flyer { position: relative; width: 846px; height: 1200px; overflow: hidden; background: var(--white); font-family: "Arimo", Arial, sans-serif; color: var(--ink); }

  .brand { position: absolute; left: 30px; top: 62px; display: flex; align-items: center; gap: 12px; }
  .brand-dot { width: 34px; height: 34px; border-radius: 50%; background: var(--magenta); }
  .brand-name { font-family: "Arimo", Arial, sans-serif; font-weight: 700; font-size: 40px; color: var(--magenta); letter-spacing: 1px; text-transform: uppercase; }

  .tagline { position: absolute; left: 380px; top: 52px; width: 440px; text-align: center; font-family: "Playball", cursive; font-size: 40px; line-height: 47px; color: var(--magenta); }

  .hero { position: absolute; left: 0; top: 168px; width: 846px; height: 294px;
    background: linear-gradient(100deg, #e8e2d8 0%, #d9b08d 22%, #f1ece4 45%, #e97d2e 55%, #f2c6d4 75%, #eeeae4 100%); }

  .join-fold { position: absolute; left: 520px; top: 462px; width: 0; height: 0; border-top: 29px solid var(--purple-deep); border-left: 43px solid transparent; }
  .join-badge { position: absolute; left: 562px; top: 423px; width: 246px; height: 68px; background: var(--purple); border: 2px solid var(--white);
    display: flex; align-items: center; justify-content: center; font-family: "Merriweather", Georgia, serif; font-weight: 700; font-size: 26px; color: var(--white); }

  .convenience { position: absolute; left: 18px; top: 502px; width: 810px; text-align: center; font-family: "Parisienne", cursive; font-size: 40px; color: var(--purple); white-space: nowrap; }

  .services-title { position: absolute; left: 21px; top: 570px; font-size: 23px; color: var(--ink); }
  .services { position: absolute; left: 18px; top: 600px; width: 810px; display: flex; gap: 8px; }
  .service { width: 196px; }
  .service-photo { width: 196px; height: 164px; border: 4px solid var(--frame); }
  .service-label { margin-top: 10px; text-align: center; font-size: 16.5px; color: var(--ink); }
  .photo-pt { background: linear-gradient(135deg, #e3e6ea, #c9cdd3 60%, #9b8fb8); }
  .photo-buddy { background: linear-gradient(135deg, #d9c7a6, #c9a57a 50%, #3fa98a); }
  .photo-kick { background: linear-gradient(110deg, #d93030 0%, #f2e4dc 45%, #e8d2c4 70%, #c92626 100%); }
  .photo-group { background: linear-gradient(160deg, #b9d9ee, #d8e6f2 45%, #2e68b8); }

  .contact-title { position: absolute; left: 20px; top: 798px; font-family: "EB Garamond", Georgia, serif; font-style: italic; font-size: 33px; color: var(--ink); }
  .phone { position: absolute; left: 26px; top: 852px; display: flex; align-items: center; gap: 14px; }
  .phone-number { font-size: 64px; color: var(--ink); }
  .email { position: absolute; left: 413px; top: 852px; display: flex; align-items: center; gap: 10px; font-size: 26px; color: var(--ink); }
  .website { position: absolute; left: 413px; top: 890px; font-size: 31px; font-weight: 700; color: var(--ink); }

  .offer-band { position: absolute; left: 0; top: 941px; width: 846px; height: 259px; background: var(--brown); }
  .offer-strip { position: absolute; left: 0; top: 0; width: 846px; height: 58px; background: var(--tan); }
  .offer-photo { position: absolute; left: 0; top: 8px; width: 410px; height: 251px;
    background: linear-gradient(90deg, #e9c9a8 0%, #d7a57c 35%, #c4896b 60%, rgba(138,90,44,0) 100%); }
  .offer-note { position: absolute; right: 20px; top: 16px; font-style: italic; font-weight: 700; font-size: 21px; color: var(--white); }
  .offer-cta { position: absolute; left: 400px; top: 62px; width: 440px; text-align: center; font-size: 54px; line-height: 72px; color: var(--white); }
  .offer-terms { position: absolute; right: 20px; top: 201px; font-style: italic; font-size: 34px; color: var(--white); }
</style>
</head>
<body>
<main class="flyer">
  <header>
    <div class="brand">
      <span class="brand-dot"></span>
      <span class="brand-name">Tide Motion</span>
    </div>
    <h1 class="tagline">Better Lifestyle Starts<br>With Healthy Workout !</h1>
  </header>

  <div class="hero" role="img" aria-label="Three people doing crunches on mats in a bright studio"></div>
  <div class="join-fold"></div>
  <div class="join-badge">JOIN US NOW !</div>

  <p class="convenience">Anytime, Anywhere, At Your Own Convenience !</p>

  <h2 class="services-title">Services Provided</h2>
  <section class="services">
    <div class="service">
      <div class="service-photo photo-pt" role="img" aria-label="Trainer assisting a client with a stability ball exercise"></div>
      <p class="service-label">Personal Training</p>
    </div>
    <div class="service">
      <div class="service-photo photo-buddy" role="img" aria-label="People doing push-ups on mats in a gym"></div>
      <p class="service-label">Buddy Training</p>
    </div>
    <div class="service">
      <div class="service-photo photo-kick" role="img" aria-label="Woman in red boxing gloves in a guard stance"></div>
      <p class="service-label">Kick boxing</p>
    </div>
    <div class="service">
      <div class="service-photo photo-group" role="img" aria-label="Group class stretching together"></div>
      <p class="service-label">Outdoor Group classes</p>
    </div>
  </section>

  <h2 class="contact-title">Our contact details:</h2>
  <div class="phone">
    <svg width="34" height="52" viewBox="0 0 34 52" aria-hidden="true">
      <rect x="2" y="2" width="30" height="48" rx="4" fill="none" stroke="#1c1c1c" stroke-width="4"/>
      <rect x="8" y="8" width="18" height="12" fill="#1c1c1c"/>
      <g fill="#1c1c1c">
        <rect x="8" y="25" width="4" height="4"/><rect x="15" y="25" width="4" height="4"/><rect x="22" y="25" width="4" height="4"/>
        <rect x="8" y="32" width="4" height="4"/><rect x="15" y="32" width="4" height="4"/><rect x="22" y="32" width="4" height="4"/>
        <rect x="8" y="39" width="4" height="4"/><rect x="15" y="39" width="4" height="4"/><rect x="22" y="39" width="4" height="4"/>
      </g>
    </svg>
    <span class="phone-number">8164-5290</span>
  </div>
  <div class="email">
    <svg width="44" height="28" viewBox="0 0 44 28" aria-hidden="true">
      <rect x="2" y="2" width="40" height="24" fill="none" stroke="#1c1c1c" stroke-width="3"/>
      <path d="M2 2 L22 16 L42 2 M2 26 L17 12 M42 26 L27 12" fill="none" stroke="#1c1c1c" stroke-width="3"/>
    </svg>
    <span>daniel@tidemotion-sg.example</span>
  </div>
  <p class="website">www.tidemotion-sg.example</p>

  <section class="offer-band">
    <div class="offer-strip"></div>
    <div class="offer-photo" role="img" aria-label="Three smiling women lifting coloured dumbbells"></div>
    <p class="offer-note">We cater to all fitness level and age group.</p>
    <p class="offer-cta">Call us now for<br>a free trial !</p>
    <p class="offer-terms">Terms &amp; conditions apply</p>
  </section>
</main>
</body>
</html>
```